Business Card Design Project

I need a business card designed with these details on the front along with the logo attached on the front.

Address - 518/ 207 Wendover st Pellbrook
Website - www.quarrelinebuilders.com.au
Email - tavin@quarrelinebuilders.com.au
Fax - 1900 417 652
Mobile - 0471936058
Telephone - 1300527961
Licence number - 874062k

```html
<!DOCTYPE html>
<html lang="en">
<head>
<meta charset="utf-8">
<title>Quarreline Builders – Business Card</title>
<link rel="stylesheet" href="https://fonts.googleapis.com/css2?family=Arimo&family=Pirata+One&family=Tinos:wght@700&display=swap">
<style>
  :root {
    --page: #ffffff;
    --page-edge: #e2e2e2;
    --card-light: #ededed;
    --brown: #432a24;
    --name-brown: #3f2622;
    --mark-tan: #e3d3bd;
    --white: #ffffff;
  }
  html, body {
    margin: 0;
    padding: 0;
    width: 1200px;
    height: 1000px;
    overflow: hidden;
    background: var(--page);
  }
  .canvas {
    position: relative;
    width: 1198px;
    height: 998px;
    border: 1px solid var(--page-edge);
    background: var(--page);
  }
  .card {
    position: absolute;
    left: 46px;
    top: 158px;
    width: 1110px;
    height: 684px;
    background: var(--card-light);
    overflow: hidden;
  }
  .card-wave {
    position: absolute;
    left: 0;
    top: 0;
    width: 1110px;
    height: 684px;
  }
  .licence {
    position: absolute;
    left: 52px;
    top: 34px;
    margin: 0;
    font-family: "Pirata One", serif;
    font-size: 33px;
    color: var(--name-brown);
  }
  .brand {
    position: absolute;
    left: 236px;
    top: 119px;
    display: flex;
    align-items: center;
    gap: 30px;
  }
  .brand-square {
    width: 150px;
    height: 150px;
    background: var(--mark-tan);
  }
  .brand-name {
    margin: 0;
    font-family: "Tinos", serif;
    font-weight: 700;
    font-size: 55px;
    line-height: 70px;
    letter-spacing: 2px;
    color: var(--name-brown);
  }
  .contact-main {
    position: absolute;
    left: 44px;
    top: 484px;
    margin: 0;
    font-family: "Arimo", sans-serif;
    font-size: 31px;
    line-height: 42px;
    color: var(--white);
    font-style: normal;
  }
  .contact-divider {
    position: absolute;
    left: 652px;
    top: 487px;
    width: 5px;
    height: 120px;
    background: linear-gradient(to right, #9a9a9a, #ffffff, #b0b0b0);
  }
  .contact-numbers {
    position: absolute;
    left: 684px;
    top: 492px;
    margin: 0;
    font-family: "Arimo", sans-serif;
    font-size: 28px;
    line-height: 35px;
    letter-spacing: 1.5px;
    color: var(--white);
    font-style: normal;
  }
  .contact-main span,
  .contact-numbers span { display: block; white-space: nowrap; }
</style>
</head>
<body>
<div class="canvas">
  <section class="card">
    <svg class="card-wave" viewBox="0 0 1110 684" aria-hidden="true">
      <path fill="var(--brown)" d="M0 267 C60 267 100 271 140 278 C260 300 470 360 600 365 C700 368 760 340 860 310 C960 282 1050 278 1110 279 V684 H0 Z"/>
    </svg>

    <p class="licence">Licence Number: 874062k</p>

    <div class="brand">
      <div class="brand-square"></div>
      <h1 class="brand-name">QUARRELINE<br>BUILDERS</h1>
    </div>

    <address class="contact-main">
      <span>518/ 207 Wendover st Pellbrook</span>
      <span>www.quarrelinebuilders.com.au</span>
      <span>tavin@quarrelinebuilders.com.au</span>
    </address>

    <div class="contact-divider"></div>

    <address class="contact-numbers">
      <span>Fax: 1900 417 652</span>
      <span>Mobile: 0471936058</span>
      <span>Telephone: 1300527961</span>
    </address>
  </section>
</div>
</body>
</html>
```